Darwell Label design search/01

We need a label design for a new customers chemical products. The label is 275mm wide and 165mm high. The design will be simple with lots of space left for us to thermally print the information required on each label. This thermal print is black. From the top down 70mm the label will be white. The logo size will be about 50mm-55mm across and 40mm-45mm down. The logo position needs to be 1 of the following positions
a) Cetred at the bottom
b) Centred at the top
c) At the bottom no closer than 70mm to the right edge
The attached logo has 8 logos on it and we would like the Darwell Chemicals on the left.
Requirements
Must have
- Logo
- look at attached info
Nice to have
- Simple and clean

```html
<!DOCTYPE html>
<html lang="en">
<head>
<meta charset="utf-8">
<title>Darwell Chemicals – Product Label</title>
<link href="https://fonts.googleapis.com/css2?family=Open+Sans:wght@700&display=swap" rel="stylesheet">
<style>
  :root {
    --brand-red: #a91e27;
    --label-white: #ffffff;
    --backdrop: #e9e6e2;
  }
  * { margin: 0; padding: 0; box-sizing: border-box; }
  html, body {
    width: 1200px;
    height: 936px;
    overflow: hidden;
    background: var(--backdrop);
  }
  .canvas {
    position: relative;
    width: 1200px;
    height: 936px;
  }
  .label {
    position: absolute;
    left: 50px;
    top: 138px;
    width: 1100px;
    height: 660px;
    background: linear-gradient(
      to bottom,
      var(--label-white) 0%,
      var(--label-white) 35%,
      #f6d9db 42%,
      #e48d93 52%,
      #c9525b 63%,
      #b3313a 72%,
      var(--brand-red) 84%,
      var(--brand-red) 100%
    );
  }
  .brand {
    position: absolute;
    top: 70px;
    left: 0;
    right: 0;
    text-align: center;
    font-family: "Open Sans", Arial, sans-serif;
    font-weight: 700;
    color: var(--brand-red);
    line-height: 1;
  }
  .brand-name {
    display: block;
    font-size: 52px;
    letter-spacing: 2px;
    text-transform: uppercase;
  }
  .brand-descriptor {
    display: block;
    margin-top: 14px;
    font-size: 18px;
    letter-spacing: 0.5px;
    text-transform: uppercase;
  }
</style>
</head>
<body>
  <main class="canvas">
    <section class="label" aria-label="Darwell Chemicals product label">
      <h1 class="brand">
        <span class="brand-name">Darwell</span>
        <span class="brand-descriptor">Chemicals</span>
      </h1>
    </section>
  </main>
</body>
</html>
```